Etiketten-Design für Nahrungsergänzungsmittel
Zielgruppe
Die Firma vertreibt Nahrungsergänzungsmittel, gesunde Lebensmittel, Lifestyle und Wellnessprodukte. Dies vor allem im Fitness und Sport Bereich. Die Marke und das entsprechende Logo sollen auf eine jüngere Zielgruppe 25+ ausgerichtet sein. Personen die für Ihren Körper und Gesundheit Sport treiben und zusätzlich Unterstützung benötigen. Die Produkte werden über Pictoloop durch eine Fitnesstrainerin beworben, und hauptsächlich über Varuno vertrieben. Produkte sind z. B. Produkte zur Ausdauersteigerung, verbesserte Konzentration, Schlaf, Stressbewältigung. Protein Shakes oder Vitamine für Veganer. No gos, Diät Produkte 5kg in 3 Tagen, Potenzsteigerung, Brustvergrößerung oder ähnliches.
Aufgabenstellung
Das Etikett wird auf einen wiederverschließbaren schwarz matten Kraftpapier Beutel im Format 28x20cm aufgebracht. Der Beutel und auch das Etikett sind kompostierbar, sieht aber beides hochwertig aus. Das Produkt ist ein veganes Proteinpulver zum anrühren mit Wasser oder Milchalternative. Einen ersten Entwurf habe ich hochgeladen.

```html
<!DOCTYPE html>
<html lang="de">
<head>
<meta charset="utf-8">
<title>LIORA – Veganer Protein Shake Etikett</title>
<link rel="stylesheet" href="https://fonts.googleapis.com/css2?family=Open+Sans:wght@400;600&family=Montserrat:wght@800&family=Orbitron:wght@600&family=Bebas+Neue&family=Quicksand:wght@500&family=Caveat:wght@500&display=swap">
<style>
  :root{
    --bg:#252525;
    --panel-dark:#1d1b1c;
    --cream:#fce6bd;
    --row-cream:#f3e2bd;
    --row-white:#ffffff;
    --text-light:#f0f0f0;
    --ink:#1e1e1e;
    --teal:#1aa394;
    --divider:#f4f4f4;
  }
  *{margin:0;padding:0;box-sizing:border-box}
  html,body{width:1200px;height:857px;overflow:hidden;background:var(--bg)}
  .label{position:relative;width:1200px;height:857px;overflow:hidden;background:var(--bg);font-family:"Open Sans",sans-serif;color:var(--text-light)}
  .divider{position:absolute;left:597px;top:0;width:4px;height:857px;background:var(--divider)}

  /* front */
  .brand-mark{position:absolute;left:266px;top:68px}
  .brand-box{position:absolute;left:96px;top:345px;width:419px;height:117px;background:var(--panel-dark);display:flex;align-items:center;justify-content:center}
  .brand-name{font-family:"Montserrat",sans-serif;font-weight:800;font-size:112px;letter-spacing:4px;color:#fff;line-height:1}
  .product-title{position:absolute;left:0;width:597px;text-align:center;font-family:"Orbitron",sans-serif;font-weight:600;color:var(--cream);line-height:1;font-size:72px}
  .t1{top:522px;letter-spacing:3px;padding-left:37px}
  .t2{top:616px;letter-spacing:4px;padding-left:38px}
  .t3{top:710px;letter-spacing:3px;padding-left:37px}

  /* back */
  .photo-layer{z-index:0}
  .text-layer{position:relative;z-index:1}
  .descr{position:absolute;left:628px;top:30px;font-size:18.2px;line-height:18px}
  .ingredients{position:absolute;left:628px;top:92px;font-size:17px;line-height:17.3px}
  .section-head{position:absolute;font-family:"Bebas Neue",sans-serif;font-size:23px;letter-spacing:2.2px;color:#fff;line-height:1}
  .nut-head{left:628px;top:187px;background:#333;padding:0 2px}
  .nut-col{top:190px}
  .nutrition{position:absolute;left:628px;top:210px;border-collapse:separate;border-spacing:6px 5px;margin:-5px -6px;font-family:"Quicksand",sans-serif;font-size:13.5px;color:var(--ink)}
  .nutrition td{height:22px;padding:0 4px}
  .nutrition td.lbl{width:215px}
  .nutrition td.val{width:110px;text-align:center}
  .nutrition tr.energy td{height:30px;line-height:13px}
  .nutrition tr:nth-child(odd) td{background:var(--row-cream)}
  .nutrition tr:nth-child(even) td{background:var(--row-white)}
  .vanilla{position:absolute;left:1080px;top:210px;width:112px;height:220px;border-radius:50% 40% 50% 45%;background:radial-gradient(circle at 55% 38%,#f4d63a 0 28%,#e8c12c 38%,#6b3f1c 60%,transparent 72%)}
  .amino-head{left:628px;top:452px}
  .amino{position:absolute;left:628px;top:477px;border-collapse:separate;border-spacing:3px 2px;margin:-2px -3px;font-family:"Quicksand",sans-serif;font-size:16px;color:var(--ink)}
  .amino td{height:19.8px;padding:0 4px;line-height:1}
  .amino td.lbl{width:84px}
  .amino td.val{width:57px;text-align:center}
  .amino tr:nth-child(odd) td{background:var(--row-cream)}
  .amino tr:nth-child(even) td{background:var(--row-white)}
  .usage{position:absolute;left:632px;top:626px;font-size:15.5px;line-height:15.5px}
  .greeting{position:absolute;left:843px;top:622px;font-family:"Caveat",cursive;font-size:23px;line-height:27px;color:var(--teal)}
  .social{position:absolute;left:847px;top:692px;display:flex;align-items:center;gap:8px}
  .social-dot{width:34px;height:34px;border-radius:50%;background:var(--teal)}
  .social-name{font-size:22px;color:var(--teal)}
  .address{position:absolute;left:628px;top:740px;font-size:17px;line-height:17px}
  .address .firm{font-size:18.5px}
  .contents{position:absolute;left:843px;top:746px;font-size:16.8px;line-height:17px}
  .trainer-photo{position:absolute;left:1074px;top:519px;width:118px;height:338px;border-radius:60px 60px 0 0;background:linear-gradient(180deg,#c9a987 0%,#b48d70 28%,#5b6877 45%,#2b2b30 75%,#1d1d20 100%)}
</style>
</head>
<body>
<div class="label">
  <section class="front">
    <svg class="brand-mark" width="80" height="80" viewBox="0 0 80 80" aria-hidden="true"><circle cx="40" cy="40" r="36" fill="none" stroke="var(--cream)" stroke-width="6"/></svg>
    <div class="brand-box"><span class="brand-name">LIORA</span></div>
    <div class="product-title t1">VEGANER</div>
    <div class="product-title t2">PROTEIN</div>
    <div class="product-title t3">SHAKE</div>
  </section>

  <div class="divider"></div>

  <section class="back">
    <div class="photo-layer">
      <div class="vanilla" role="img" aria-label="Illustration einer gelben Vanilleblüte mit Vanilleschoten"></div>
      <div class="trainer-photo" role="img" aria-label="Foto der Fitnesstrainerin in Sportkleidung mit verschränkten Armen"></div>
    </div>

    <div class="text-layer">
      <p class="descr">Getränkepulver zur Herstellung eines veganen Eiweißgetränkes<br>mit Süßungsmittel - Geschmacksrichtung Vanille</p>
      <p class="ingredients">Zutaten: Eiweißmischung (93 %) Erbseneiweiß, Reiseiweiß,<br>Hanfsamenpulver, Bio Kürbiskerneiweiß, Aroma,<br>Verdickungsmittel: Xanthan, Kokosnussmilchpulver,<br>Süßungsmittel: Sucralose</p>

      <div class="section-head nut-head">NÄHRWERTANGABEN PRO</div>
      <div class="section-head nut-col" style="left:882px">100G</div>
      <div class="section-head nut-col" style="left:970px">PORTION = 30G</div>
      <table class="nutrition">
        <tr class="energy"><td class="lbl">Energie</td><td class="val">1.9694 kJ<br>401 kcal</td><td class="val">1.9694 kJ<br>401 kcal</td></tr>
        <tr><td class="lbl">- davon gesättigte Fettsäuren</td><td class="val">8,3 g</td><td class="val">8,3 g</td></tr>
        <tr><td class="lbl">Kohlenhydrate</td><td class="val">8,3 g</td><td class="val">8,3 g</td></tr>
        <tr><td class="lbl">- davon Zucker</td><td class="val">8,3 g</td><td class="val">8,3 g</td></tr>
        <tr><td class="lbl">Ballaststoffe</td><td class="val">8,3 g</td><td class="val">8,3 g</td></tr>
        <tr><td class="lbl">Eiweiß</td><td class="val">8,3 g</td><td class="val">8,3 g</td></tr>
        <tr><td class="lbl">Salz</td><td class="val">8,3 g</td><td class="val">8,3 g</td></tr>
        <tr><td class="lbl">Fett</td><td class="val">8,3 g</td><td class="val">8,3 g</td></tr>
      </table>

      <div class="section-head amino-head">AMINOSÄURENPROFIL PRO 100G EIWEISS</div>
      <table class="amino">
        <tr><td class="lbl">Eiweiß</td><td class="val">4,4 g</td><td class="lbl">Eiweiß</td><td class="val">4,4 g</td><td class="lbl">Eiweiß</td><td class="val">4,4 g</td></tr>
        <tr><td class="lbl">Eiweiß</td><td class="val">4,4 g</td><td class="lbl">Eiweiß</td><td class="val">4,4 g</td><td class="lbl">Eiweiß</td><td class="val">4,4 g</td></tr>
        <tr><td class="lbl">Eiweiß</td><td class="val">4,4 g</td><td class="lbl">Eiweiß</td><td class="val">4,4 g</td><td class="lbl">Eiweiß</td><td class="val">4,4 g</td></tr>
        <tr><td class="lbl">Eiweiß</td><td class="val">4,4 g</td><td class="lbl">Eiweiß</td><td class="val">4,4 g</td><td class="lbl">Eiweiß</td><td class="val">4,4 g</td></tr>
        <tr><td class="lbl">Eiweiß</td><td class="val">4,4 g</td><td class="lbl">Eiweiß</td><td class="val">4,4 g</td><td class="lbl">Eiweiß</td><td class="val">4,4 g</td></tr>
        <tr><td class="lbl">Eiweiß</td><td class="val">4,4 g</td><td class="lbl">Eiweiß</td><td class="val">4,4 g</td><td class="lbl">Eiweiß</td><td class="val">4,4 g</td></tr>
      </table>

      <p class="usage">Verzehrempfehlung:<br>30 g Pulver im 300 ml<br>Wasser lösen; Das<br>Produkt ist kühl, trocken<br>und dunkel zu lagern.</p>

      <p class="greeting">Besuche mich auf Pictoloop!<br>liebe Grüße Liora</p>
      <div class="social"><span class="social-dot"></span><span class="social-name">liorabyliora</span></div>

      <p class="address"><span class="firm">LIORA UG</span><br>Lindenhofweg 12<br>76999 Talbrunn<br>info@liorabyliora.de</p>
      <p class="contents">Inhalt: 600 g Eiweißpulver<br>für 20 Shakes<br>Mindestens haltbar bis Ende<br>08/2023; Losnr.: 977109</p>
    </div>
  </section>
</div>
</body>
</html>
```